Crimson Badger Soil Works - Car Wraps

1:. i had some logos made, I will upload the variations and stationary Designs I picked. So you can see the colors and styles that i like.

2:. main design will be for a 2015 vxr tundoro 2500 hd SLT 4x4 torquelin
But need it so that it can be adjusted to other work trucks with different lengths. They will be vxrs as well. Just some with single cab or shorter beds.

3.: Mainly want the sides and truck bed back side on tailgate.
3.1 : Update: after seeing a few with just sides,. I am open to seeing fuller or full wraps as well.
(I added one pic that i saw in the bright easel that is close to my trucks,
3.2 : UPDATE2: just added more pics of the model that is very close to mine, mine is a silver metalic, But that is the shape
I will add for ideas.)

Added new video and pictures of some of my equipment in action

Target Market(s)

Farmers, Agriculture industry, State contractors, labor contractors

Industry/Entity Type

Agriculture, Farming, Excivation, Earth Moving

Font styles to use
Serif
Sans Serif

Colors

Designer to choose colors to be used in the design.

Requirements
Nice to have
• Striping to match the attached Logos, and stationary . that may make it go all together as a identity. but I am open to your creativity

```html
<!DOCTYPE html>
<html lang="en">
<head>
<meta charset="utf-8">
<title>Crimson Badger Soil Works – Truck Wrap</title>
<link href="https://fonts.googleapis.com/css2?family=Montserrat:wght@800&display=swap" rel="stylesheet">
<style>
  :root {
    --wrap-red: #8e0f12;
    --wrap-red-dark: #6f0a0d;
    --wrap-green: #7cc242;
    --glass: #c9c9c9;
    --arch: #222222;
    --tyre: #1c1c1c;
    --rim: #9a9a9a;
    --mark-grey: #b9b9b9;
    --page: #ffffff;
  }
  html, body {
    margin: 0;
    width: 1200px;
    height: 1200px;
    overflow: hidden;
    background: var(--page);
  }
  .wrap-sheet { display: block; width: 1200px; height: 1200px; }
  .body-red { fill: var(--wrap-red); }
  .band-green { fill: var(--wrap-green); }
  .window { fill: var(--glass); }
  .wheel-arch { fill: var(--arch); }
  .tyre { fill: var(--tyre); }
  .rim { fill: var(--rim); }
  .brand-square { fill: var(--mark-grey); }
  .phone, .brand-name, .web {
    font-family: "Montserrat", Arial, sans-serif;
    font-weight: 800;
  }
  .phone { fill: #fff; font-size: 15px; }
  .brand-name { fill: var(--wrap-green); }
  .brand-name-main { font-size: 17px; }
  .brand-name-sub { font-size: 12px; letter-spacing: 1.5px; }
  .web { fill: var(--wrap-red-dark); font-size: 10px; }
</style>
</head>
<body>
<svg class="wrap-sheet" viewBox="0 0 1200 1200" xmlns="http://www.w3.org/2000/svg">
  <defs>
    <clipPath id="truck-body">
      <path d="M60,215 L235,198 L330,135 L560,125 Q585,128 588,190 L892,190 L895,300 L880,325 L805,325 A65,65 0 0 0 675,325 L250,330 A68,68 0 0 0 115,330 L62,330 Z"/>
    </clipPath>
    <linearGradient id="fade-green" x1="0" y1="0" x2="1" y2="0">
      <stop offset="0" stop-color="#7cc242" stop-opacity="0"/>
      <stop offset="1" stop-color="#7cc242" stop-opacity="0.95"/>
    </linearGradient>
    <linearGradient id="site-photo" x1="0" y1="0" x2="0" y2="1">
      <stop offset="0" stop-color="#7ea3c9"/>
      <stop offset="0.3" stop-color="#b7c3c9"/>
      <stop offset="0.45" stop-color="#d9b73a"/>
      <stop offset="0.7" stop-color="#a68b68"/>
      <stop offset="1" stop-color="#8a7560"/>
    </linearGradient>

    <g id="truck-paint">
      <rect class="body-red" x="50" y="110" width="860" height="240"/>
      <polygon class="band-green" points="575,185 600,185 535,335 262,335 262,315 505,315"/>
      <polygon fill="url(#site-photo)" role="img" aria-label="Photo of bulldozers and ripping equipment on a dirt job site"
               points="600,190 895,190 895,280 660,335 535,335"/>
      <polygon class="band-green" points="660,335 895,278 895,335"/>
    </g>

    <g id="truck-details">
      <path class="window" d="M300,205 L345,150 L420,148 L420,203 Z"/>
      <path class="window" d="M445,147 L545,145 Q552,146 552,160 L552,198 L445,200 Z"/>
      <path class="wheel-arch" d="M112,332 A70,70 0 0 1 252,332 Z"/>
      <path class="wheel-arch" d="M672,328 A68,68 0 0 1 808,328 Z"/>
      <circle class="tyre" cx="182" cy="350" r="58"/>
      <circle class="rim" cx="182" cy="350" r="34"/>
      <circle class="tyre" cx="740" cy="350" r="58"/>
      <circle class="rim" cx="740" cy="350" r="34"/>

      <text class="phone" x="115" y="247">555-014-2837</text>

      <rect class="brand-square" x="380" y="228" width="36" height="36"/>
      <text class="brand-name brand-name-main" x="398" y="289" text-anchor="middle">CRIMSON BADGER</text>
      <text class="brand-name brand-name-sub" x="398" y="305" text-anchor="middle">SOIL WORKS</text>
      <text class="web" x="398" y="327" text-anchor="middle">crimsonbadgersoilworks.com</text>
    </g>
  </defs>

  <g class="option-fade" transform="scale(1.25)">
    <g clip-path="url(#truck-body)">
      <use href="#truck-paint"/>
      <polygon fill="url(#fade-green)" points="430,120 600,120 600,190 575,190 505,315 430,315"/>
    </g>
    <use href="#truck-details"/>
  </g>

  <g class="option-diagonal" transform="scale(1.25) translate(0,430)">
    <g clip-path="url(#truck-body)">
      <use href="#truck-paint"/>
    </g>
    <use href="#truck-details"/>
  </g>
</svg>
</body>
</html>
```